Brochure Cover Design Project

Need a design for our company brochure cover.
We are a mechanical consulting engineering firm ( HVAC, pLUMBING). We have the brochure

Target Market(s)

Architects and Building Owners

Industry/Entity Type

Hvac

```html
<!DOCTYPE html>
<html lang="en">
<head>
<meta charset="utf-8">
<title>Alderpoint Mechanical — Brochure Cover</title>
<link rel="stylesheet" href="https://fonts.googleapis.com/css2?family=Archivo+Black&family=Carlito:wght@400;700&display=swap">
<style>
  :root {
    --brand-green: #4b8a3e;
    --headline-green: #3f8a3c;
    --bright-green: #7ed348;
    --bright-green-edge: #4f9a2e;
    --ink: #111111;
    --paper: #ffffff;
    --tile-pale: #eef0ef;
    --tile-pale-2: #e4e8e6;
  }
  * { margin: 0; padding: 0; box-sizing: border-box; }
  html, body { width: 873px; height: 1200px; overflow: hidden; background: var(--paper); }
  .cover {
    position: relative;
    width: 873px;
    height: 1200px;
    background: var(--paper);
    font-family: "Carlito", "Calibri", sans-serif;
  }
  .masthead-band {
    position: absolute; left: 46px; top: 112px; width: 827px; height: 54px;
    background: var(--brand-green);
  }
  .wordmark {
    position: absolute; left: 188px; top: 62px;
    font-family: "Archivo Black", sans-serif;
    font-size: 44px; line-height: 1;
    color: var(--headline-green);
    letter-spacing: 1px;
  }
  .photo { position: absolute; }
  .photo--main { border-bottom: 2px solid #e8e8e8; }
  .photo--faded { background: linear-gradient(160deg, var(--tile-pale), var(--tile-pale-2)); opacity: .75; }
  .headline { position: absolute; left: 0; top: 0; }
  .strip-dot { position: absolute; width: 5px; height: 5px; }
  .tagline {
    position: absolute; right: 39px; top: 858px; width: 760px;
    text-align: right; color: var(--headline-green);
    font-size: 23.5px; line-height: 33px;
  }
  .tagline .initial { font-size: 37px; line-height: 1; }
  .company-band {
    position: absolute; left: 0; top: 992px; width: 467px; height: 57px;
    background: var(--brand-green);
    display: flex; align-items: center; padding-left: 31px;
    font-size: 25px; color: var(--ink); letter-spacing: .2px;
  }
  .contact {
    position: absolute; left: 31px; top: 1059px;
    font-size: 16px; line-height: 22px; color: var(--ink);
    list-style: none;
  }
</style>
</head>
<body>
<main class="cover">
  <div class="masthead-band"></div>
  <div class="wordmark">ALDERPOINT</div>

  <!-- project photography column -->
  <div class="photo photo--faded" style="left:54px;top:374px;width:105px;height:52px" role="img" aria-label="Faded building facade detail"></div>
  <div class="photo photo--faded" style="left:264px;top:426px;width:159px;height:109px" role="img" aria-label="Faded office building exterior"></div>
  <div class="photo photo--faded" style="left:161px;top:534px;width:52px;height:57px" role="img" aria-label="Faded lobby detail"></div>
  <div class="photo photo--faded" style="left:423px;top:537px;width:157px;height:57px" role="img" aria-label="Faded atrium interior"></div>
  <div class="photo photo--faded" style="left:54px;top:594px;width:105px;height:51px" role="img" aria-label="Faded canopy detail"></div>
  <div class="photo photo--faded" style="left:127px;top:646px;width:33px;height:52px" role="img" aria-label="Faded column detail"></div>
  <div class="photo photo--faded" style="left:161px;top:705px;width:159px;height:109px" role="img" aria-label="Faded corridor interior"></div>
  <div class="photo photo--faded" style="left:321px;top:705px;width:159px;height:109px" role="img" aria-label="Faded clinic reception interior"></div>

  <div class="photo photo--main" style="left:0;top:262px;width:160px;height:111px;background:linear-gradient(180deg,#a9c3de 0%,#d6e0ea 45%,#c9cccd 70%,#7d8184 100%)" role="img" aria-label="Two-storey medical office building under a blue sky"></div>
  <div class="photo photo--main" style="left:160px;top:371px;width:160px;height:107px;background:linear-gradient(180deg,#6f98c6 0%,#9fb6c7 30%,#5f7f78 60%,#b7b3aa 100%)" role="img" aria-label="Glass-fronted office building entrance"></div>
  <div class="photo photo--main" style="left:0;top:481px;width:160px;height:110px;background:linear-gradient(180deg,#1d3c86 0%,#3b5aa0 40%,#b48a4e 70%,#5a4530 100%)" role="img" aria-label="Curved building canopy lit at dusk"></div>
  <div class="photo photo--main" style="left:160px;top:593px;width:160px;height:109px;background:linear-gradient(90deg,#cfd2cf 0%,#eef0ee 45%,#8fb7ae 75%,#dfe3e1 100%)" role="img" aria-label="Bright lobby interior with glass walls and plants"></div>
  <div class="photo photo--main" style="left:0;top:704px;width:160px;height:111px;background:linear-gradient(180deg,#a77a4a 0%,#d8c6a6 35%,#e6ddcc 60%,#8f8a82 100%)" role="img" aria-label="Hospital reception desk interior"></div>

  <svg class="headline" width="873" height="760" viewBox="0 0 873 760" aria-label="Engineering the art of the possible">
    <text x="183" y="354" textLength="651" lengthAdjust="spacingAndGlyphs"
          font-family="Archivo Black, sans-serif" font-size="103" fill="var(--headline-green)" stroke="#2e6b2c" stroke-width="1">ENGINEERING</text>
    <text x="559" y="443" textLength="275" lengthAdjust="spacingAndGlyphs"
          font-family="Archivo Black, sans-serif" font-size="72" fill="#ffffff" stroke="#8a8a8a" stroke-width="1.4">THE ART</text>
    <text x="601" y="533" textLength="233" lengthAdjust="spacingAndGlyphs"
          font-family="Archivo Black, sans-serif" font-size="74" fill="var(--ink)">OF THE</text>
    <text x="347" y="668" textLength="487" lengthAdjust="spacingAndGlyphs"
          font-family="Archivo Black, sans-serif" font-size="105" fill="var(--bright-green)" stroke="var(--bright-green-edge)" stroke-width="1.2">POSSIBLE</text>
  </svg>

  <!-- thumbnail strip -->
  <div class="photo" style="left:487px;top:701px;width:61px;height:41px;background:linear-gradient(180deg,#2a2a40,#8a3a2a)" role="img" aria-label="Auditorium interior"></div>
  <div class="photo" style="left:550px;top:701px;width:111px;height:41px;background:linear-gradient(90deg,#2c4a8a,#1f2f4a 50%,#c49a6a)" role="img" aria-label="Modern building at night and interior hall"></div>
  <div class="photo" style="left:674px;top:701px;width:70px;height:41px;background:linear-gradient(180deg,#c9d3db,#8c7f6e)" role="img" aria-label="Residential building facade"></div>
  <div class="photo" style="left:748px;top:701px;width:86px;height:41px;background:linear-gradient(180deg,#cfd9e2,#e9ecee 50%,#7a8a72)" role="img" aria-label="Historic glass conservatory"></div>
  <span class="strip-dot" style="left:503px;top:744px;background:#3f8a3c"></span>
  <span class="strip-dot" style="left:511px;top:744px;background:#3f8a3c"></span>
  <span class="strip-dot" style="left:530px;top:744px;border:1px solid #7ed348"></span>
  <span class="strip-dot" style="left:579px;top:744px;background:#3f8a3c"></span>
  <span class="strip-dot" style="left:698px;top:744px;background:#7ed348"></span>
  <span class="strip-dot" style="left:706px;top:744px;background:#3f8a3c"></span>
  <span class="strip-dot" style="left:739px;top:744px;border:1px solid #7ed348"></span>
  <span class="strip-dot" style="left:755px;top:744px;background:#3f8a3c"></span>
  <span class="strip-dot" style="left:785px;top:744px;background:#7ed348"></span>
  <span class="strip-dot" style="left:799px;top:744px;background:#3f8a3c"></span>

  <p class="tagline"><span class="initial">O</span>ur art is seeing green, comfortable, elegant and functional building<br>systems made possible. This is the passion that drives our work.</p>

  <div class="company-band">ALDERPOINT MECHANICAL inc.</div>
  <ul class="contact">
    <li>2450 Cedar Ridge Rd. Ste. 210</li>
    <li>Maple Hollow, CA 94000</li>
    <li>Tel 555-014-0100 x 106</li>
    <li>Fax 555-014-0144</li>
  </ul>
</main>
</body>
</html>
```